Folder and brochures for food service software solution

We offer integrated software solutions for independent and chain food service businesses. Such businesses would include fine dining restaurants, fast food outlets, home delivery, takeaways, cafeterias, event catering venues, institutional catering companies, hotels with restaurants / bars, etc. Our software is configured for the needs of each type of business and spans both guest facing and back office functions.

The core benefits our solution offers is that it is -
1. integrated to cater to all the needs of the food service business, both independent and chain, across most (not all, we do not do anything for labor management) functions.
2. functionally powerful and compare well with the best available internationally.
3. Developed using the latest in software technology ... for example, our EPOS software for Android devices.

The market is a mature market with many competitors. A few very well established with huge track record. We have a track record internationally but are new to the UK market. This brochure is targeted at the UK market. The target market is jaded with the number of options available. We will focus on fine dining outlets in the hope that our Android based EPOS will excite them. We will focus on events & catering because the competition in the segment is relatively thin. We will go after the institutional catering market because we offer strong cost control features. But we want to mention how we service all sub-segments of the food & beverage service business to convey the versatility of our solution and for the other businesses that we may be able to attract.

We are hoping that the brochure will stand-out from the crowd and will compel the market to browse through what we do.

Some key competitors in the UK include -
http://www.varnobi.co.uk/
http://www.q-tel.co.uk/
http://www.harmdock.co.uk/
http://vemoru.co.uk/

We have a company and product logo (both attached). Of these, we are open to dropping or redesgning the product logo. We have also developed a web site (see gdqk.brantowell.com). The brochure design need not conform to the web site, if (and only if) you can come up with a really attention design (we could consider redesign of the web site).

The content of the brochure will largely conform to the content at the web site. The content at the web site is structured by solutions for independent outlets (centered around the EPOS) and solutions for chains. It also mentions 18 products. This is too much for a print brochure. So, we propose the following structure -

1. a folder that also carries a brief about our company with facility to add inserts.
2. one brochure that describes the solutions offered, the market segments they apply to and the benefits of the solution for each segment.
3. A summary / list of the products that are used to configure the solution.

We will add product specific flyers to the folder by color laser printing these. This will provide us the flexibility to add only the few product sheets that are of relevance to each prospect and will allow us to update frequently. For this we will require a template so that all product sheets look similar ... possibly with a color theme separating the products for each outlet from those for the chain of outlets.

We can only provide low-res images. You will have to touch up screens to improve resolution of images to make them print-ready. You are free to propose purchase of reasonably priced general stock-shots subject to prior approval from us. We will pay for these images.
Updates

At least one of you have requested that we -

1. identify a key message and

2. compact the contents of the brochure 

To do so, we have had to take an alternative approach and revise the content completely. Please check back and see the latest uploads, both Mirelle - Approach 2 and Mirelle - Salient Features.

We hope this helps you in your design effort.                     

Reason: We understand that we are requesting this design through a holiday season. We are extending the deadline by a few days. If this also does not work for some of you, please let us know a realistic date by which you are able to provide us options. We will consider, even though we are on a tight time line.

Reason: Some of you are still working on final layouts At least one of you is waiting for us to provide you modified content to fit the design. The extra days are intended to allow you to provide a complete and final design.

Earlier, we had posted an update and new content. This was in response to the community's request to reduce content. Did you note that? It seems not. So, we have now removed older content and only retained the revised content as per the last update. Please verify that the design you propose is as per the latest content. In the process, we may have removed some images also. Need them? Let me know and I will re-post.

Reason: Further extension, open only to those that have previously submitted designs and need the extra time to finalize the design based on feedback from us.

Target Market(s)

Upper mid market fine dining restaurants, likely with home delivery / takeaway options.
Small food service chains (3 to 10 outlets).
Venues with catering facilities.
Cafeterias.
Bulk food suppliers / institutional caterers.
Food service business with a central kitchen / commissary and multiple service locations.
membership clubs with food service.

Industry/Entity Type

Software

Font styles to use
Sans Serif

Requirements
Must have
• A distinctive attention grabbing design.

The structure of -
1. a folder with facility for inserts.
2. two brochures.
3. template for product specific write-ups.
Nice to have
• Info-graphics to represent an integrated solution. Another to demonstrate versatility across types of F&B business.

A design that relates the solution to the UK ... either in terms of colors or visuals.

```html
<!DOCTYPE html>
<html lang="en">
<head>
<meta charset="utf-8">
<title>Mirelle – Integrated Software Solution</title>
<link href="https://fonts.googleapis.com/css2?family=Exo+2:wght@300;400;600;700&display=swap" rel="stylesheet">
<style>
  :root{
    --red:#c4161c;
    --red-deep:#8e0d12;
    --red-bright:#e0262b;
    --ink:#3a3a3a;
    --grey-head:#8a8a8a;
    --paper:#ffffff;
    --paper-shade:#e6e6e8;
    --photo-dark:#1c2233;
    --photo-mid:#3d4f7a;
    --photo-light:#9fb0d6;
  }
  html,body{margin:0;padding:0;overflow:hidden;}
  body{width:841px;height:1200px;position:relative;
    background:linear-gradient(to bottom,var(--paper) 0%,var(--paper) 50%,var(--paper-shade) 100%);
    font-family:"Exo 2",Arial,sans-serif;color:var(--ink);}
  .hero{position:absolute;left:0;top:0;width:841px;height:400px;}
  .hero svg{display:block}
  .testimonial{position:absolute;left:46px;top:118px;width:292px;
    font-size:11.6px;line-height:13.4px;font-weight:700;color:#fff;text-align:justify;margin:0;}
  .testimonial cite{display:block;font-style:normal;color:var(--red-bright);text-align:left;}
  .intro-title,.section-title{position:absolute;left:36px;margin:0;font-weight:700;color:var(--red-deep);}
  .intro-title{top:396px;font-size:30px;}
  .intro-text{position:absolute;left:40px;top:428px;width:770px;margin:0;
    font-size:15.6px;line-height:19px;font-weight:300;text-align:justify;}
  .offer{position:absolute;left:34px;top:502px;margin:0;font-size:28px;font-weight:700;color:var(--grey-head);}
  .section-title{font-size:28px;}
  .feature-icon{position:absolute;left:38px;}
  .feature-text{position:absolute;left:204px;width:606px;margin:0;font-weight:300;text-align:justify;}
  .feature-text.small{font-size:12.8px;line-height:19.5px;text-align:left;}
  .feature-text.large{font-size:15.6px;line-height:19.6px;}
  .feature-text ul{margin:0;padding:0;list-style:none;}
  .feature-text li::before{content:"▪ ";}
</style>
</head>
<body>
  <div class="hero">
    <svg width="841" height="400" viewBox="0 0 841 400">
      <defs>
        <linearGradient id="room" x1="0" y1="0" x2="1" y2="1">
          <stop offset="0" stop-color="var(--photo-dark)"/>
          <stop offset="0.5" stop-color="var(--photo-mid)"/>
          <stop offset="1" stop-color="var(--photo-light)"/>
        </linearGradient>
      </defs>
      <polygon points="0,326 841,222 841,266 0,388" fill="var(--red)"/>
      <polygon points="0,0 841,0 841,246 0,348" fill="url(#room)" role="img" aria-label="Photograph of an elegant restaurant dining room with laid tables under blue light"/>
      <rect x="36" y="0" width="314" height="330" fill="#000" opacity="0.35"/>
    </svg>
    <p class="testimonial">"I have been very pleased with the deployment of Mirelle and the after sales support from Brantowell. We now have a system that gives us ample reports which makes business decisions easier. The Guest Profiler allows us to keep on track with our Customers changing requirements and also stores whether a previous Diner/Customer has special dietary requirements. The delivery module has enhanced user experience. Having these features in place, we can make business decisions based on the collection of data we gather from Mirelle.
      <cite>Arun Mehrotra<br>Director, Saffron Court - London</cite></p>
  </div>

  <h2 class="intro-title">Made Easy</h2>
  <p class="intro-text">No longer do you need to struggle to fit your business process and information needs to available software solutions. You do not need to compromise your innovative business strategies because your software has limitations.</p>

  <h1 class="offer">WE OFFER YOU MIRELLE.</h1>

  <h2 class="section-title" style="top:540px">Integrated Software Solution</h2>
  <svg class="feature-icon" style="top:600px" width="136" height="140" viewBox="0 0 136 140">
    <defs>
      <radialGradient id="disc" cx="0.4" cy="0.35" r="0.7">
        <stop offset="0" stop-color="var(--red-bright)"/><stop offset="1" stop-color="var(--red-deep)"/>
      </radialGradient>
      <linearGradient id="rim" x1="0" y1="0" x2="0" y2="1"><stop offset="0" stop-color="#fff"/><stop offset="1" stop-color="#bcbcbc"/></linearGradient>
    </defs>
    <ellipse cx="68" cy="132" rx="50" ry="6" fill="#000" opacity="0.15"/>
    <circle cx="68" cy="66" r="66" fill="url(#rim)"/>
    <circle cx="68" cy="66" r="56" fill="url(#disc)"/>
    <g fill="#fff">
      <circle cx="60" cy="52" r="15"/><circle cx="60" cy="52" r="20" fill="none" stroke="#fff" stroke-width="7" stroke-dasharray="6 5"/>
      <circle cx="88" cy="80" r="10"/><circle cx="88" cy="80" r="14" fill="none" stroke="#fff" stroke-width="5" stroke-dasharray="5 4"/>
      <circle cx="44" cy="84" r="7"/><circle cx="44" cy="84" r="10" fill="none" stroke="#fff" stroke-width="4" stroke-dasharray="4 3"/>
    </g>
    <g fill="var(--red)"><circle cx="60" cy="52" r="5"/><circle cx="88" cy="80" r="4"/><circle cx="44" cy="84" r="3"/></g>
  </svg>
  <div class="feature-text small" style="top:600px">
    We have developed an array of software tools that can be configured to deliver you the benefits of an integrated IT solution that caters to most of your functional needs. A solution –
    <ul>
      <li>Where data flows, and is visible, across functional departments electronically,</li>
      <li>That works out of a single computer server, is easier to administer &amp; costs less,</li>
      <li>Is supported by a single helpdesk that does not deflect responsibility to anyone else and</li>
      <li>Can interface with the 3rd party product(s) that you are happy to use.</li>
    </ul>
  </div>

  <h2 class="section-title" style="top:764px">For Your Specific Needs</h2>
  <svg class="feature-icon" style="top:820px" width="136" height="140" viewBox="0 0 136 140">
    <ellipse cx="68" cy="132" rx="50" ry="6" fill="#000" opacity="0.15"/>
    <circle cx="68" cy="66" r="66" fill="url(#rim)"/>
    <circle cx="68" cy="66" r="56" fill="url(#disc)"/>
    <g fill="none" stroke="#fff" stroke-width="6" stroke-linejoin="round">
      <rect x="30" y="58" width="76" height="16" transform="rotate(45 68 66)"/>
      <path d="M44 44 L92 92 M40 96 L96 40" transform="translate(0 0)"/>
    </g>
  </svg>
  <p class="feature-text large" style="top:826px">Mirelle offers tools allow you to configure a solution that is specific to your needs. Irrespective of whether yours is an independent or chain business. Irrespective of whether your business includes one or more of fine dining, casual dining, in-hotel food service, quick service, events catering, contract catering, cafeteria or other type of food service outlet(s). You will find that Mirelle offers special exceptional benefits for each type of business.</p>

  <h2 class="section-title" style="top:988px">Superior Reporting</h2>
  <svg class="feature-icon" style="top:1044px" width="136" height="140" viewBox="0 0 136 140">
    <ellipse cx="68" cy="132" rx="50" ry="6" fill="#000" opacity="0.15"/>
    <circle cx="68" cy="66" r="66" fill="url(#rim)"/>
    <circle cx="68" cy="66" r="56" fill="url(#disc)"/>
    <g fill="#fff" stroke="var(--red)" stroke-width="2">
      <rect x="56" y="28" width="38" height="50"/>
      <rect x="48" y="36" width="38" height="50"/>
      <rect x="40" y="44" width="38" height="52"/>
    </g>
    <g fill="var(--red)"><rect x="47" y="58" width="24" height="4"/><rect x="47" y="67" width="24" height="4"/><rect x="47" y="76" width="24" height="4"/></g>
  </svg>
  <p class="feature-text large" style="top:1048px">The standard reports included with Mirelle are amongst the nest available in the industry. It provides comprehensive insights into operations and your business. Reports can be delivered electronically, to you, by email. Or, you can log in with your mobile for an instant flash.</p>
</body>
</html>
```